New Fernwick 4 Loop waste management business seeking web site

New project for business offering sustainable options within the waste industry.
Business called Fernwick 4 Loop
Targeting the consumer & industry professionals the web site needs to be able to accommodate both.
Needs to have a modern clean feel.
Logo being designed by another pro and will be completed early next week and will be submitted soon after to be incorporated into the web page
Links to another web page i like very much to take into consideration.

Target Market(s)

Industry professionals, consumers and producers of all waste, Food, constructruction, commercial, retail .. etc..

Industry/Entity Type

Waste Management

Coding

Coded - Design and coding required

Number of Pages Required

5+ page

Font styles to use
Serif
Script

Requirements
Must have
• Flexabilty, all pages as in examples
Nice to have
• Open to offers you guys and gals are the pro's

```html
<!DOCTYPE html>
<html lang="en">
<head>
<meta charset="utf-8">
<title>Fernwick 4 Loop</title>
<link rel="stylesheet" href="https://fonts.googleapis.com/css2?family=Cinzel:wght@400;700&family=Open+Sans:wght@400;600;700&family=Oswald:wght@500;700&family=Arimo:wght@400;700&display=swap">
<style>
:root{
  --black:#050505;
  --dark:#1c1c1c;
  --green:#4b7d0c;
  --green-bright:#4f8f12;
  --lime:#b6ef6a;
  --red:#b5130f;
  --text:#2b2b2b;
  --muted:#8a8a8a;
  --blush:#fdf6f4;
  --sand:#efece6;
  --row:#f3f4f7;
  --white:#ffffff;
}
*{margin:0;padding:0;box-sizing:border-box}
html,body{width:1200px;height:2671px;overflow:hidden}
body{font-family:"Open Sans",sans-serif;color:var(--text);background:var(--white);position:relative}

/* header */
.site-header{position:absolute;top:0;left:0;width:1200px;height:75px;background:linear-gradient(#1a1a1a,var(--black))}
.brand{position:absolute;left:135px;top:24px;display:flex;align-items:center;gap:10px;color:var(--white);font-family:"Cinzel",serif;font-weight:700;font-size:18px}
.brand-dot{width:22px;height:22px;border-radius:50%;background:var(--red)}
.main-nav a{position:absolute;top:26px;color:var(--white);font-family:"Cinzel",serif;font-size:16px;text-decoration:none;letter-spacing:.5px}

/* hero */
.hero{position:absolute;top:75px;left:0;width:1200px;height:491px;background:linear-gradient(180deg,#b8ef6f 0%,#b3ec68 60%,#a9e25d 100%)}
.hero-photo{position:absolute;inset:0;background:linear-gradient(100deg,rgba(120,170,60,.25),rgba(220,255,170,.15) 45%,rgba(110,160,50,.28))}
.social{position:absolute;top:18px;width:30px;height:30px;border-radius:50%;border:2px solid rgba(255,255,255,.85)}
.hero-mark{position:absolute;top:84px;left:0;width:1200px;display:flex;justify-content:center;align-items:center;gap:8px;font-family:"Cinzel",serif;font-weight:700;font-size:18px;color:var(--red)}
.hero-mark span.dot{width:18px;height:18px;border-radius:50%;background:var(--red)}
.hero-title{position:absolute;top:146px;width:1200px;text-align:center;font-family:"Cinzel",serif;font-weight:400;font-size:34px;color:#111}
.hero-tag{position:absolute;top:196px;width:1200px;text-align:center;font-family:"Oswald",sans-serif;font-weight:700;font-size:18px;color:var(--red)}
.how{position:absolute;top:262px;left:490px;font-family:"Arimo",sans-serif;font-weight:400;font-size:35px;color:#111}
.how-arrow{position:absolute;top:268px;left:424px}
.step-icon{position:absolute;top:350px;width:82px;height:72px;background:rgba(60,110,20,.45);border-radius:8px}
.step-text{position:absolute;top:343px;width:215px;font-family:"Arimo",sans-serif;font-weight:700;font-size:15px;line-height:21px;color:#1a1a1a}

/* welcome */
.welcome{position:absolute;top:566px;left:0;width:1200px;height:292px;background:var(--white)}
.section-title{position:absolute;width:1200px;text-align:center;font-family:"Cinzel",serif;font-weight:700;font-size:33px;color:var(--green)}
.title-rule{position:absolute;left:555px;width:90px;height:3px;background:var(--red)}
.lede{position:absolute;left:132px;width:936px;text-align:center;font-size:12px;line-height:22px;color:#333}
.btn-more{position:absolute;width:100px;height:34px;border:1px dashed var(--green);font-size:12px;font-weight:700;color:#222;display:flex;align-items:center;justify-content:center;letter-spacing:.3px;background:var(--white)}

/* services */
.services{position:absolute;top:858px;left:0;width:1200px;height:326px;background:var(--blush);border-top:1px solid #f2dedb;border-bottom:1px solid #f2dedb}
.svc{position:absolute;top:0;width:290px;height:326px}
.svc-icon{position:absolute;top:37px;left:114px;width:62px;height:48px;background:#3a3a3a;border-radius:3px}
.svc-title{position:absolute;top:94px;width:290px;text-align:center;font-family:"Cinzel",serif;font-weight:700;font-size:24px;color:var(--red)}
.svc-text{position:absolute;top:133px;width:290px;text-align:center;font-size:12px;line-height:22.5px;color:#333}
.svc .btn-more{top:242px;left:95px}

/* what we do */
.what{position:absolute;top:1184px;left:0;width:1200px;height:361px;background:var(--white)}
.figure{position:absolute;top:98px;left:132px;width:160px;height:217px;border-radius:6px;background:linear-gradient(180deg,#d9d9d9,#8c8c8c)}
.task{position:absolute;left:317px;width:751px;height:33px;background:var(--row);border-left:3px solid #c9ccd3;font-size:12px;color:#222;padding-left:16px;display:flex;align-items:center}

/* news */
.news{position:absolute;top:1545px;left:0;width:1200px;height:333px;background:var(--sand)}
.post{position:absolute;top:0;width:431px}
.post-head{position:absolute;top:110px;font-size:13.5px;font-weight:400;color:var(--red);white-space:nowrap}
.post-date{position:absolute;top:138px;font-size:11px;color:var(--muted)}
.post-body{position:absolute;top:163px;width:431px;font-size:12px;line-height:21.5px;color:#222}
.post-more{position:absolute;top:265px;font-size:11px;font-weight:700;color:#222}
.news-divider{position:absolute;left:598px;top:128px;width:1px;height:180px;background:#d5d0c6}

/* contact */
.contact{position:absolute;top:1878px;left:0;width:1200px;height:748px;background:var(--dark)}
.contact .section-title{color:var(--red);font-weight:400}
.contact-lede{position:absolute;top:91px;left:340px;width:520px;text-align:center;font-size:13px;line-height:21px;color:#e4e4e4}
.newsletter{position:absolute;top:162px;left:132px;width:936px;height:84px;background:#000}
.env{position:absolute;top:16px;left:14px;width:50px;height:50px;border-radius:50%;background:var(--white)}
.nl-title{position:absolute;top:10px;left:84px;font-size:16px;color:var(--green-bright)}
.nl-sub{position:absolute;top:33px;left:84px;font-size:13px;line-height:20px;color:#f0f0f0}
.field-label{position:absolute;top:10px;font-size:12px;color:#f0f0f0}
.field{position:absolute;top:36px;width:225px;height:34px;background:#2e2e2e}
.subscribe{position:absolute;top:38px;left:795px;width:114px;height:32px;background:var(--green-bright);color:var(--white);font-size:15px;font-weight:700;display:flex;align-items:center;justify-content:center}
.info-head{position:absolute;top:264px;font-size:16px;font-weight:400;color:var(--green-bright)}
.info-line{position:absolute;font-size:13px;color:#eaeaea}
.info-line.active{color:var(--red)}
.ico{position:absolute}
.footer-name{position:absolute;top:285px;left:940px;width:140px;text-align:center;font-family:"Cinzel",serif;font-weight:700;font-size:18px;line-height:24px;color:#3a3a3a}
.map{position:absolute;top:408px;left:132px;width:936px;height:310px;background:linear-gradient(135deg,#ecebe2,#e3e1d4 50%,#ecead9)}

.site-footer{position:absolute;top:2626px;left:0;width:1200px;height:45px;background:#000;color:#d8d8d8;font-size:12px;display:flex;align-items:center;justify-content:center}
</style>
</head>
<body>

<header class="site-header">
  <div class="brand"><span class="brand-dot"></span>Fernwick 4 Loop</div>
  <nav class="main-nav">
    <a style="left:415px">Home</a>
    <a style="left:508px">About</a>
    <a style="left:602px">Services</a>
    <a style="left:713px">Recycling</a>
    <a style="left:842px">Our Team</a>
    <a style="left:968px">Contacts</a>
  </nav>
</header>

<section class="hero">
  <div class="hero-photo" role="img" aria-label="Recycling yard with baled waste, tinted lime green"></div>
  <span class="social" style="left:903px"></span>
  <span class="social" style="left:947px"></span>
  <span class="social" style="left:991px"></span>
  <span class="social" style="left:1035px"></span>
  <div class="hero-mark"><span class="dot"></span>Fernwick 4 Loop</div>
  <h1 class="hero-title">Fernwick 4 Loop</h1>
  <p class="hero-tag">DELIVERING THE BEST WASTE AND RECYCLING SOLUTIONS</p>
  <svg class="how-arrow" width="60" height="40" viewBox="0 0 60 40"><path d="M56 6 C36 4 20 12 12 30" fill="none" stroke="#111" stroke-width="2"/><path d="M5 24 L12 32 L18 22" fill="none" stroke="#111" stroke-width="2"/></svg>
  <h2 class="how">How does it work</h2>

  <div class="step-icon" style="left:132px" role="img" aria-label="Recycling bin icon"></div>
  <p class="step-text" style="left:224px">Consectetuer adipiscingelit, sed diam nonummy nibh eu ismod tincidunt ut laoreet dolore.</p>
  <div class="step-icon" style="left:459px" role="img" aria-label="Collection truck icon"></div>
  <p class="step-text" style="left:553px">Consectetuer adipiscingelit, sed diam nonummy nibh eu ismod tincidunt ut laoreet dolore.</p>
  <div class="step-icon" style="left:783px" role="img" aria-label="Recycling arrows icon"></div>
  <p class="step-text" style="left:878px">Consectetuer adipiscingelit, sed diam nonummy nibh eu ismod tincidunt ut laoreet dolore.</p>
</section>

<section class="welcome">
  <h2 class="section-title" style="top:42px">Welcome to Fernwick 4 Loop</h2>
  <span class="title-rule" style="top:92px"></span>
  <p class="lede" style="top:120px">Lorem ipsum dolor sit amet, consectetuer adipiscing elit, sed diam nonummy nibh euismod tincidunt ut laoreet dolore magna aliquam erat volutpat. Ut wisi enim ad minim veniam, quis nostrud exerci tation ullamcorper suscipit lobortis nisl ut aliquip ex ea commodo consequat. Duis autem vel eum iriure dolor in hendrerit in vulputate velit esse molestie consequat, vel illum dolore eu feugiat nulla facilisis at vero eros et accumsan.</p>
  <span class="btn-more" style="top:210px;left:550px">READ MORE</span>
</section>

<section class="services">
  <div class="svc" style="left:126px">
    <div class="svc-icon" role="img" aria-label="House icon"></div>
    <h3 class="svc-title">Residential</h3>
    <p class="svc-text">Lorem ipsum dolor sit amet, consectetuer adipiscing elit, sed diam nonummy nibh euismod tincidunt ut laoreet dolore magna aliquam erat volutpat. Ut wisi enim ad minim.</p>
    <span class="btn-more">READ MORE</span>
  </div>
  <div class="svc" style="left:455px">
    <div class="svc-icon" role="img" aria-label="Office building icon"></div>
    <h3 class="svc-title">Commercial</h3>
    <p class="svc-text">Lorem ipsum dolor sit amet, consectetuer adipiscing elit, sed diam nonummy nibh euismod tincidunt ut laoreet dolore magna aliquam erat volutpat. Ut wisi enim ad minim.</p>
    <span class="btn-more">READ MORE</span>
  </div>
  <div class="svc" style="left:783px">
    <div class="svc-icon" role="img" aria-label="Handshake icon"></div>
    <h3 class="svc-title">Join Us</h3>
    <p class="svc-text">Lorem ipsum dolor sit amet, consectetuer adipiscing elit, sed diam nonummy nibh euismod tincidunt ut laoreet dolore magna aliquam erat volutpat. Ut wisi enim ad minim.</p>
    <span class="btn-more">READ MORE</span>
  </div>
</section>

<section class="what">
  <h2 class="section-title" style="top:38px">What we Do ?</h2>
  <div class="figure" role="img" aria-label="Illustrated businessman in a grey suit gesturing toward the list"></div>
  <div class="task" style="top:105px">Lorem ipsum dolor sit amet, consectetuer adipiscing elit, sed diam nonummy nibh euismod tincidunt ut laoreet.</div>
  <div class="task" style="top:149px">Laoreet dolore magna aliquam erat volutpat. Ut wisi enim ad minim.</div>
  <div class="task" style="top:193px">Sed diam nonummy nibh euismod tincidunt ut laoreet dolore magna</div>
  <div class="task" style="top:237px">Tincidunt ut laoreet dolore magna aliquam erat volutpat. Ut wisi enim ad minim.</div>
  <div class="task" style="top:281px">Dolor sit amet, consectetuer adipiscing elit, sed diam nonummy</div>
</section>

<section class="news">
  <h2 class="section-title" style="top:40px">Latest News</h2>
  <article class="post" style="left:132px">
    <h4 class="post-head">Lorem ipsum dolor sit amet, consectetuer adipiscing elit, sed dia.</h4>
    <p class="post-date">Thursday, December10,2015</p>
    <p class="post-body">Lorem ipsum dolor sit amet, consectetuer adipiscing elit, sed diam nonummy nibh euismod tincidunt ut laoreet dolore magna aliquam erat volutpat. Ut wisi enim ad minim. Lorem ipsum dolor sit amet, consectetuer adipiscing elit, sed diam nonummy nibh euismod tincidunt.</p>
    <span class="post-more">READ MORE »</span>
  </article>
  <div class="news-divider"></div>
  <article class="post" style="left:637px">
    <h4 class="post-head">Lorem ipsum dolor sit amet, consectetuer adipiscing elit, sed dia.</h4>
    <p class="post-date">Thursday, December10,2015</p>
    <p class="post-body">Lorem ipsum dolor sit amet, consectetuer adipiscing elit, sed diam nonummy nibh euismod tincidunt ut laoreet dolore magna aliquam erat volutpat. Ut wisi enim ad minim. Lorem ipsum dolor sit amet, consectetuer adipiscing elit, sed diam nonummy nibh euismod tincidunt.</p>
    <span class="post-more">READ MORE »</span>
  </article>
</section>

<section class="contact">
  <h2 class="section-title" style="top:38px">Contact Us</h2>
  <p class="contact-lede">Lorem ipsum dolor sit amet, consectetuer adipiscing elit, sed dianonummy nibh euismod tincidunt ut laoreet.</p>

  <div class="newsletter">
    <div class="env">
      <svg width="50" height="50" viewBox="0 0 50 50"><rect x="14" y="17" width="22" height="16" fill="none" stroke="#222" stroke-width="2"/><path d="M14 17 L25 27 L36 17" fill="none" stroke="#222" stroke-width="2"/></svg>
    </div>
    <p class="nl-title">Newsletter Sign-up</p>
    <p class="nl-sub">Lorem ipsum doamet,<br>consectetuer adipiscing elit.</p>
    <span class="field-label" style="left:318px">First Name</span>
    <span class="field" style="left:318px"></span>
    <span class="field-label" style="left:552px">Email Address</span>
    <span class="field" style="left:552px"></span>
    <span class="subscribe">SUBSCRIBE</span>
  </div>

  <h5 class="info-head" style="left:132px">Contact information:</h5>
  <p class="info-line" style="left:132px;top:295px">Halden Studio AS</p>
  <p class="info-line" style="left:132px;top:322px">Mara Lindqvist</p>
  <p class="info-line" style="left:132px;top:349px">Partner demo</p>

  <h5 class="info-head" style="left:404px">Address:</h5>
  <svg class="ico" style="left:404px;top:297px" width="12" height="16" viewBox="0 0 12 16"><path d="M6 1 a5 5 0 0 1 5 5 c0 4 -5 9 -5 9 s-5 -5 -5 -9 a5 5 0 0 1 5 -5z" fill="#8a8a8a"/><circle cx="6" cy="6" r="2" fill="#1c1c1c"/></svg>
  <p class="info-line" style="left:434px;top:295px">Vell 9, 4120 Brekkby</p>
  <svg class="ico" style="left:403px;top:324px" width="14" height="14" viewBox="0 0 14 14"><path d="M3 1 l3 3 -2 2 c1 2 2 3 4 4 l2 -2 3 3 -2 2 c-5 0 -10 -5 -10 -10z" fill="#8a8a8a"/></svg>
  <p class="info-line" style="left:434px;top:322px">+01 987 65 432</p>
  <svg class="ico" style="left:403px;top:353px" width="16" height="12" viewBox="0 0 16 12"><rect x="0" y="0" width="16" height="12" fill="#8a8a8a"/><path d="M0 0 L8 7 L16 0" fill="none" stroke="#1c1c1c" stroke-width="1.5"/></svg>
  <p class="info-line" style="left:434px;top:349px">info@f4l-mail.com</p>

  <h5 class="info-head" style="left:662px">Quick Links:</h5>
  <p class="info-line active" style="left:662px;top:295px">→ Home</p>
  <p class="info-line" style="left:662px;top:322px">→ About</p>
  <p class="info-line" style="left:662px;top:349px">→ Services</p>
  <p class="info-line" style="left:769px;top:295px">→ Recycling</p>
  <p class="info-line" style="left:769px;top:322px">→ Our Team</p>
  <p class="info-line" style="left:769px;top:349px">→ Contacts</p>

  <p class="footer-name">Fernwick<br>4 Loop</p>

  <div class="map" role="img" aria-label="City street map showing the office location"></div>
</section>

<footer class="site-footer">All Rights Reserved 2015 © Fernwick 4 Loop</footer>

</body>
</html>
```